business card for a massage therapy practice named 'Meadow and Willow Massage Studio'

I really need a trendy, yet easy on the eyes business card to complement my logo. Ideally with some gold or rose gold foil work.

My uploaded file of the logo I have in horizontal but I have a vertical version as well. Another color that is used in the website is a blush pink here and there. I'd like to see some trendy tropical leaves in the design.

```html
<!DOCTYPE html>
<html lang="en">
<head>
<meta charset="utf-8">
<title>Meadow and Willow Massage Studio — Business Card</title>
<link href="https://fonts.googleapis.com/css2?family=Lato:wght@400;700&family=Dancing+Script:wght@600&display=swap" rel="stylesheet">
<style>
  :root{
    --bg:#d9d9d9;
    --bg-deep:#a3a3a3;
    --blush-light:#fdf1f0;
    --blush:#f7d9d8;
    --coral:#f2838f;
    --plum:#5a1f2c;
    --ink:#2b2b2b;
    --text:#4a3a3d;
    --rule:#e9a9ad;
    --leaf-light:#f3d3da;
    --leaf:#d99aaa;
    --leaf-deep:#b86f85;
    --ring:#5a5a5a;
  }
  *{margin:0;padding:0;box-sizing:border-box}
  html,body{width:1200px;height:1200px;overflow:hidden}
  body{
    background:linear-gradient(180deg,var(--bg) 0%,var(--bg-deep) 100%);
    font-family:"Lato",Arial,sans-serif;
    position:relative;
  }
  .card{
    position:absolute;left:160px;width:880px;height:503px;
    box-shadow:0 18px 40px rgba(0,0,0,.22);
    overflow:hidden;
  }
  /* Front */
  .card-front{
    top:70px;
    background:linear-gradient(160deg,var(--blush) 0%,var(--blush-light) 55%,#fff8f7 100%);
  }
  .brand{
    position:absolute;left:60px;top:120px;width:300px;
    display:flex;align-items:center;gap:14px;
  }
  .brand-dot{width:34px;height:34px;border-radius:50%;background:#c8a97a;flex:none}
  .brand-name{font-weight:700;font-size:26px;line-height:1.15;color:var(--ink)}
  .divider{position:absolute;width:1px;background:var(--rule)}
  .divider-name{left:395px;top:105px;height:105px}
  .divider-contact{left:395px;top:255px;height:170px}
  .person{position:absolute;left:425px;top:110px}
  .person-name{font-family:"Dancing Script",cursive;font-size:58px;color:var(--plum);line-height:1}
  .person-role{font-size:20px;color:var(--text);margin-top:4px}
  .contact{position:absolute;left:425px;top:262px;list-style:none;color:var(--text);font-size:21px}
  .contact li{display:flex;align-items:flex-start;gap:12px;margin-bottom:10px}
  .contact svg{width:18px;height:18px;flex:none;margin-top:4px;fill:var(--plum)}
  .band-line{position:absolute;left:0;right:0;bottom:54px;height:6px;background:var(--coral)}
  .band{position:absolute;left:0;right:0;bottom:0;height:44px;background:var(--coral)}
  /* Back */
  .card-back{
    top:617px;
    background:linear-gradient(135deg,var(--leaf-light) 0%,var(--leaf) 45%,var(--leaf-deep) 75%,var(--leaf) 100%);
  }
  .leaf-pattern{position:absolute;inset:0}
  .seal{
    position:absolute;left:50%;top:50%;width:300px;height:300px;
    transform:translate(-50%,-50%);border-radius:50%;
    border:6px solid var(--ring);background:rgba(255,255,255,.6);
    display:flex;align-items:center;justify-content:center;text-align:center;
  }
  .seal-name{font-weight:700;font-size:36px;line-height:1.2;color:var(--ink)}
</style>
</head>
<body>
  <section class="card card-front">
    <div class="brand">
      <span class="brand-dot"></span>
      <span class="brand-name">Meadow &amp; Willow Massage Studio</span>
    </div>
    <span class="divider divider-name"></span>
    <div class="person">
      <p class="person-name">Jane Rowe</p>
      <p class="person-role">Director</p>
    </div>
    <span class="divider divider-contact"></span>
    <ul class="contact">
      <li><svg viewBox="0 0 24 24"><path d="M12 2a7 7 0 0 0-7 7c0 5 7 13 7 13s7-8 7-13a7 7 0 0 0-7-7zm0 9.5A2.5 2.5 0 1 1 12 6.5a2.5 2.5 0 0 1 0 5z"/></svg><span>Dummy city<br>Dummy Country Land</span></li>
      <li><svg viewBox="0 0 24 24"><path d="M6.6 10.8a15 15 0 0 0 6.6 6.6l2.2-2.2c.3-.3.7-.4 1-.2 1.1.4 2.3.6 3.6.6.6 0 1 .4 1 1V20c0 .6-.4 1-1 1A17 17 0 0 1 3 4c0-.6.4-1 1-1h3.5c.6 0 1 .4 1 1 0 1.3.2 2.5.6 3.6.1.3 0 .7-.2 1z"/></svg><span>1-234-555019</span></li>
      <li><svg viewBox="0 0 24 24"><path d="M2 5h20v14H2z M2 5l10 8 10-8" fill="none" stroke="currentColor"/><path d="M2 5h20l-10 8z"/><path d="M2 7l10 8 10-8v12H2z"/></svg><span>jane@meadowandwillow.com</span></li>
      <li><svg viewBox="0 0 24 24"><path d="M12 2a10 10 0 1 0 0 20 10 10 0 0 0 0-20zm6.9 6h-3a15 15 0 0 0-1.3-3.9A8 8 0 0 1 18.9 8zM12 4c.8 1.2 1.5 2.5 1.9 4h-3.8c.4-1.5 1.1-2.8 1.9-4zM4.3 14a8 8 0 0 1 0-4h3.4a16 16 0 0 0 0 4zm.8 2h3a15 15 0 0 0 1.3 3.9A8 8 0 0 1 5.1 16zm3-8h-3a8 8 0 0 1 4.3-3.9A15 15 0 0 0 8.1 8zM12 20c-.8-1.2-1.5-2.5-1.9-4h3.8c-.4 1.5-1.1 2.8-1.9 4zm2.3-6H9.7a14 14 0 0 1 0-4h4.6a14 14 0 0 1 0 4zm.3 5.9a15 15 0 0 0 1.3-3.9h3a8 8 0 0 1-4.3 3.9zM16.3 14a16 16 0 0 0 0-4h3.4a8 8 0 0 1 0 4z"/></svg><span>www.meadowandwillow.com</span></li>
    </ul>
    <span class="band-line"></span>
    <span class="band"></span>
  </section>

  <section class="card card-back">
    <div class="leaf-pattern" role="img" aria-label="Watercolour pattern of blush pink tropical monstera and palm leaves"></div>
    <div class="seal">
      <span class="seal-name">Meadow &amp;<br>Willow</span>
    </div>
  </section>
</body>
</html>
```